Bluewater Getaways KT needs a new Website

We have an old website that is just that - old. We need a fresh website that is professional graphic designed that has the following features.
1. Can be updated by ourselves in some areas.
2. Has a shopping cart.
3. Has links to download PDF files
4. Has links to other pages in the website
5. Includes social media links
6. Has a client log-in area
Full details in brief provided.

SORRY BUT IT'S URGENT. We've taken too long to write the details and it is now urgent. So my apologies I will be asking for designers to work quickly.

We will continue to use our existing web hosting company and url. Their is a link to the old website in the Design Brief.
Updates

UPDATE:  Please see the new file UPDATE TO DESIGN BRIEF.
Thanks for all your submissions to date.  We hope the update will assist with your designs.
As indicated in previous messages, we are happy with the Home Page + 1 Page in order to select the designer to work with in creating the full design. 

Thankyou Designers.  Much appreciate your efforts.
It's getting late here on Norfolk so I won't have much chance too review any more designs this evening.
But for your information:
Designer 7318405 Ravindra Mehta is so far the closest to what we are seeking.
Thanks again. 

Reason: Have extended to Monday 7 October to give time for designers to submit after feedback today. Especially given the time differences

Target Market(s)

Very wide audience. Current client group not that tech savvy, but we hope to broaden our market and sell more creative products, and so website needs to consider how people now use media, ie tablets & iphones.

Industry/Entity Type

Shopping

Requirements
Nice to have
• PLEASE SEE THE "UPDATE TO THE DESIGN BRIEF"

```html
<!DOCTYPE html>
<html lang="en">
<head>
<meta charset="utf-8">
<title>Norfolk Island – Bluewater Getaways KT</title>
<link href="https://fonts.googleapis.com/css2?family=Open+Sans:wght@400;600;700&family=Kaushan+Script&display=swap" rel="stylesheet">
<style>
:root{
  --orange:#f58220;
  --green:#1fa84f;
  --green-line:#3dbb66;
  --white:#ffffff;
  --ink:#1e1e1e;
  --mist-1:#f2f2f2;
  --mist-2:#cfd2d3;
}
*{margin:0;padding:0;box-sizing:border-box}
html,body{width:1200px;height:700px;overflow:hidden}
body{font-family:"Open Sans",Arial,sans-serif;color:var(--white);background:var(--white);position:relative}
a{color:inherit;text-decoration:underline}

/* Sidebar */
.sidebar{position:absolute;left:0;top:0;width:233px;height:700px;background:var(--green)}
.brand{position:absolute;left:0;top:0;width:233px;height:126px;background:var(--white)}
.brand-edge{position:absolute;left:0;top:124px;width:233px;height:10px}
.brand-mark{position:absolute;left:22px;top:44px;width:34px;height:34px;border-radius:50%;background:var(--orange)}
.brand-name{position:absolute;left:64px;top:36px;color:var(--orange);font-weight:600;font-size:16px;line-height:18px}
.nav{position:absolute;left:0;top:151px;width:233px;list-style:none}
.nav li{height:40px;border-bottom:1px solid var(--green-line);display:flex;align-items:center;padding-left:67px;position:relative;font-size:13.5px;line-height:16px}
.nav li.active{background:var(--orange);border-bottom-color:var(--orange)}
.nav svg{position:absolute;left:25px;top:9px;width:22px;height:22px;fill:var(--white)}
.book-btn{position:absolute;left:32px;top:644px;width:157px;height:40px;background:var(--orange);display:flex;align-items:center;padding-left:45px;font-size:17px;text-decoration:none}
.book-btn svg{position:absolute;left:11px;top:8px;width:22px;height:22px;fill:var(--white)}

/* Intro column */
.intro{position:absolute;left:233px;top:0;width:255px;height:700px;background:var(--orange);padding:45px 12px 0 22px}
.intro h1{font-size:28px;font-weight:700;letter-spacing:.2px;margin-left:4px;margin-bottom:24px}
.intro p{font-size:11.4px;line-height:16px;margin-bottom:16px;margin-left:2px;letter-spacing:-.2px;hyphens:auto;-webkit-hyphens:auto}

/* Feature column */
.feature{position:absolute;left:488px;top:0;width:545px;height:700px;color:var(--ink)}
.feature-bg{position:absolute;inset:0;background:linear-gradient(160deg,var(--mist-1) 0%,#e2e4e4 45%,var(--mist-2) 100%)}
.feature h2{position:absolute;left:66px;top:30px;font-family:"Kaushan Script",cursive;font-weight:400;font-size:35px;color:var(--ink)}
.activities{position:absolute;left:56px;top:92px;width:430px;font-size:14.5px;line-height:24px}
.more-btn{position:absolute;left:168px;top:190px;width:186px;height:48px;background:var(--orange);color:var(--white);font-size:18px;display:flex;align-items:center;padding-left:48px;text-decoration:none}
.more-btn svg{position:absolute;left:18px;top:11px;width:24px;height:24px;fill:var(--white)}
.gallery{position:absolute;left:28px;top:278px;width:478px;height:306px;display:grid;grid-template-columns:repeat(3,1fr);grid-template-rows:repeat(2,1fr);box-shadow:0 2px 8px rgba(0,0,0,.3)}
.gallery div:nth-child(1){background:linear-gradient(180deg,#7fb3de,#a88a62)}
.gallery div:nth-child(2){background:linear-gradient(180deg,#5a8fc8,#7d8a4c)}
.gallery div:nth-child(3){background:linear-gradient(180deg,#6e8f63,#8fb35c)}
.gallery div:nth-child(4){background:linear-gradient(180deg,#6c5a48,#d9d6cf)}
.gallery div:nth-child(5){background:linear-gradient(180deg,#7d8a86,#6a5138)}
.gallery div:nth-child(6){background:linear-gradient(180deg,#3f6a78,#2fa3c3)}
.links-title{position:absolute;left:28px;top:598px;font-family:"Kaushan Script",cursive;font-weight:400;font-size:21px}
.links{position:absolute;top:634px;font-size:12px;line-height:18px}
.links.left{left:28px}
.links.right{left:287px}

/* Contact column */
.contact{position:absolute;left:1033px;top:0;width:167px;height:700px;background:var(--green);text-align:center;font-size:10.4px;line-height:12.5px}
.panel-head{background:var(--orange);font-weight:700;font-size:15.5px;line-height:19px;letter-spacing:.3px}
.panel-head.location{height:71px;padding-top:18px}
.panel-head.media{position:absolute;left:0;top:392px;width:167px;height:42px;padding-top:12px;font-size:16px}
.ico{width:18px;height:18px;border-radius:50%;background:var(--white);margin:0 auto 4px;display:flex;align-items:center;justify-content:center}
.ico svg{width:11px;height:11px;fill:var(--green)}
.c-block{position:absolute;left:0;width:167px}
.support{position:absolute;left:0;top:567px;width:167px;font-weight:700;font-size:15px}
.merch{position:absolute;left:15px;top:588px;width:104px;height:56px;background:linear-gradient(120deg,#f3a33b,#e9e7e2 55%,#3a3a3a)}
.shop-btn{position:absolute;left:13px;top:654px;width:136px;height:36px;background:var(--orange);font-size:17px;display:flex;align-items:center;padding-left:38px;text-decoration:none}
.shop-btn svg{position:absolute;left:10px;top:7px;width:22px;height:22px;fill:var(--white)}
</style>
</head>
<body>

<aside class="sidebar">
  <div class="brand">
    <span class="brand-mark"></span>
    <span class="brand-name">Bluewater<br>Getaways KT</span>
  </div>
  <svg class="brand-edge" viewBox="0 0 233 10" preserveAspectRatio="none"><path fill="#ffffff" d="M0 0H233V4l-4 4-4-4-4 4-4-4-4 4-4-4-4 4-4-4-4 4-4-4-4 4-4-4-4 4-4-4-4 4-4-4-4 4-4-4-4 4-4-4-4 4-4-4-4 4-4-4-4 4-4-4-4 4-4-4-4 4-4-4-4 4-4-4-4 4-4-4-4 4-4-4-4 4-4-4-4 4-4-4-4 4-4-4-4 4-4-4-4 4-4-4-4 4-4-4-4 4-4-4-4 4-4-4-4 4-4-4-4 4-4-4-4 4-4-4-4 4-4-4-4 4-4-4-4 4-4-4-4 4-4-4-4 4-4-4-4 4-4-4-4 4-4-4-4 4-4-4-4 4-4-4-4 4-4-4-4 4-4-4-4 4-4-4-4 4-4-4-4 4-4-4-4 4-4-4-4 4-4-4-4 4-4-4-4 4-4-4-4 4-4-4-4 4-4-4-4 4-4-4-4 4-4-4-4 4-1 1Z"/></svg>

  <ul class="nav">
    <li><svg viewBox="0 0 24 24"><path d="M12 3 2 12h3v9h5v-6h4v6h5v-9h3z"/></svg>Home</li>
    <li><svg viewBox="0 0 24 24"><path d="M4 3h11v18H4zM16 9h4v12h-4zM6 6v2h2V6zm4 0v2h2V6zM6 10v2h2v-2zm4 0v2h2v-2zM6 14v2h2v-2zm4 0v2h2v-2z"/></svg>Governance</li>
    <li class="active"><svg viewBox="0 0 24 24"><path d="M11 8C9 5 5 5 3 7c3-1 5 0 7 2-3 0-5 2-5 4 2-2 4-3 6-3l-3 11h3l2-11c2 1 4 3 4 6 1-3 0-6-3-7 3-1 5 0 7 1-1-3-5-4-8-2 0-2 1-4 3-5-3 0-5 2-5 5z"/></svg>Norfolk Island</li>
    <li><svg viewBox="0 0 24 24"><path d="M4 2h12l4 4v16H4zm6 6a4 4 0 1 0 0 8 4 4 0 0 0 0-8zm3 8 4 4 1-1-4-4z"/></svg>Our Mission<br>and Values</li>
    <li><svg viewBox="0 0 24 24"><path d="M5 4h3V2h6v2h3v9a6 6 0 0 0-7 8H5zm11 10a4 4 0 1 1 0 8 4 4 0 0 1 0-8zm-2 4 1.5 1.5L18 17"/></svg>Services</li>
    <li><svg viewBox="0 0 24 24"><path d="M12 2a4 4 0 1 1 0 8 4 4 0 0 1 0-8zM5 22v-5c0-3 3-5 7-5s7 2 7 5v5z"/></svg>Our Facilitator</li>
    <li><svg viewBox="0 0 24 24"><path d="M3 3h18v4H3zM4 9h16v12h-6v-7H9v7H4z"/></svg>Our Shop</li>
    <li><svg viewBox="0 0 24 24"><path d="M12 5a3 3 0 1 1 0 6 3 3 0 0 1 0-6zM5 7a2.5 2.5 0 1 1 0 5 2.5 2.5 0 0 1 0-5zm14 0a2.5 2.5 0 1 1 0 5 2.5 2.5 0 0 1 0-5zM7 19c0-3 2-6 5-6s5 3 5 6zM1 18c0-2 1-4 4-4 1 0 2 .5 2 1-1 1-1.5 2-1.5 3zm22 0h-4.5c0-1-.5-2-1.5-3 0-.5 1-1 2-1 3 0 4 2 4 4z"/></svg>Holiday Programs</li>
    <li><svg viewBox="0 0 24 24"><path d="M6 10h12l-2 12H8zM8 2l2 7H9L7 3zm5 0h1v7h-1zm5 1 1 1-3 5h-1z"/></svg>Design your own<br>Norfolk Island Holiday</li>
    <li><svg viewBox="0 0 24 24"><circle cx="12" cy="5" r="3"/><circle cx="5" cy="18" r="3"/><circle cx="19" cy="18" r="3"/><path d="M11 8h2v4l4 4-1 1-4-4-4 4-1-1 4-4z"/></svg>cWV Creative Projects</li>
    <li><svg viewBox="0 0 24 24"><circle cx="6" cy="4" r="2.5"/><circle cx="17" cy="4" r="2.5"/><path d="M4 8h4v14H6v-6H5v6H3V8zm11 0h4v14h-2v-6h-1v6h-2V8zM8 8l3-3 1 1-4 4zm7 0-3-3-1 1 4 4z"/></svg>Schoolies, Siblings &amp;<br>and Family Holidays</li>
    <li><svg viewBox="0 0 24 24"><path d="M12 4c6 0 10 3 10 6.5S18 17 12 17c-1 0-2 0-3-.3L4 19l1.5-3.5C3 14 2 12.3 2 10.5 2 7 6 4 12 4z"/></svg>Testimonials</li>
  </ul>

  <a class="book-btn"><svg viewBox="0 0 24 24"><path d="M12 2a4 4 0 1 1 0 8 4 4 0 0 1 0-8zM6 14h12v4H6zM3 20h18v2H3z"/></svg>Book Now</a>
</aside>

<section class="intro">
  <h1>Norfolk Island</h1>
  <p>Norfolk Island is more than a picturesque island in the South Pacific; it is paradise with a past. &nbsp;What was once a convict’s nightmare is now the tranquil home of the descendants from the Mutiny on the Bounty, who have their own unique cul&shy;ture and language.</p>
  <p>Norfolk Island offers our groups the full range of holiday experiences in a uniquely safe and friendly place. &nbsp;Norfolk Islanders love sharing their idyllic island paradise; &nbsp;a very friendly community welcoming of all visitors.</p>
  <p>You do need a Passport to travel to Nor&shy;folk Island. &nbsp;For Australian citizens there is also the option of entering Norfolk with a Document of Identity. &nbsp;Obtaining a DOI is the same process as applying for an Australia Passport with the only differ&shy;ence being the passport is valid for travel between Australia and Norfolk Island only and is free of charge to obtain.</p>
  <p>Your holiday can be relaxing or adventur&shy;ous, may include entertaining cultural and historic tours, interactive showers where everyone gets to join in, including “a night as a convict”, great beaches, fish&shy;ing and boating, horse riding, mini-golf, arts, crafts, great shopping and much, much more....</p>
</section>

<main class="feature">
  <div class="feature-bg" role="img" aria-label="Faded photograph of tall Norfolk pine trees above the island coastline"></div>
  <h2>100 Things to do on Norfolk</h2>
  <p class="activities">Golf, Mini Golf, &nbsp;Athletics, Squash, Equestrian, Shooting, Tennis, Snooker &amp; Darts, Surfing/Swimming, Windsurfing, Water Sports<br>- Hire Service, Scuba Diving, Fishing, Hiking, shopping, hiking</p>
  <a class="more-btn"><svg viewBox="0 0 24 24"><path d="M11 8C9 5 5 5 3 7c3-1 5 0 7 2-3 0-5 2-5 4 2-2 4-3 6-3l-3 11h3l2-11c2 1 4 3 4 6 1-3 0-6-3-7 3-1 5 0 7 1-1-3-5-4-8-2 0-2 1-4 3-5-3 0-5 2-5 5z"/></svg>and a lot more</a>
  <div class="gallery">
    <div role="img" aria-label="Photo of a holiday group posing beside a large lizard sculpture"></div>
    <div role="img" aria-label="Photo of a fisherman holding up a large fish by the sea"></div>
    <div role="img" aria-label="Photo of two dancers in grass skirts performing on a lawn"></div>
    <div role="img" aria-label="Photo of a group in matching white shirts at an evening event"></div>
    <div role="img" aria-label="Photo of a horse-drawn carriage tour with passengers"></div>
    <div role="img" aria-label="Photo of a kayaker paddling in clear blue water by rocks"></div>
  </div>
  <h3 class="links-title">Links to Norfolk Island Website</h3>
  <div class="links left"><a>www.pineshoreisland.com.au</a><br><a>www.exploreislandlife.com</a></div>
  <div class="links right"><a>www.islandtravelhub.nf</a><br><a>www.greenpinetours.com</a></div>
</main>

<aside class="contact">
  <h2 class="panel-head location">LOCATION<br>AND CONTACTS</h2>

  <div class="c-block" style="top:82px">
    <div class="ico"><svg viewBox="0 0 24 24"><path d="M12 2a7 7 0 0 1 7 7c0 5-7 13-7 13S5 14 5 9a7 7 0 0 1 7-7zm0 4a3 3 0 1 0 0 6 3 3 0 0 0 0-6z"/></svg></div>
    Kingfisher Lane, Pine Hollow<br>PO Box 412<br>Norfolk Island NSW 2899<br>SOUTH PACIFIC<br>N.B.N. 147 552 806
  </div>
  <div class="c-block" style="top:175px">
    <div class="ico"><svg viewBox="0 0 24 24"><path d="M6 2l4 5-2 3c1 2 4 5 6 6l3-2 5 4-3 4C10 22 2 14 2 5z"/></svg></div>
    International + 67 23 58140<br>Australia 1800 432 617<br>New Zealand
  </div>
  <div class="c-block" style="top:241px">
    <div class="ico"><svg viewBox="0 0 24 24"><path d="M2 5h20v14H2zm2 2v1l8 5 8-5V7l-8 5z"/></svg></div>
    hello@bluewatergetaways.org
  </div>
  <div class="c-block" style="top:282px">
    <div class="ico"><svg viewBox="0 0 24 24"><path d="M12 2a10 10 0 1 1 0 20 10 10 0 0 1 0-20zm-1 2.1A8 8 0 0 0 4.1 11H8c.1-2.6.9-5 3-6.9zm2 0c2.1 1.9 2.9 4.3 3 6.9h3.9A8 8 0 0 0 13 4.1zM10 11h4c-.1-2.2-.8-4-2-5.5-1.2 1.5-1.900 3.3-2 5.5zm-5.9 2A8 8 0 0 0 11 19.9c-2.1-1.9-2.9-4.3-3-6.9zm5.9 0c.1 2.2.8 4 2 5.5 1.2-1.5 1.9-3.3 2-5.5zm6 0c-.1 2.6-.9 5-3 6.9a8 8 0 0 0 6.9-6.9z"/></svg></div>
    www.bluewatergetaways.org
  </div>
  <div class="c-block" style="top:323px">
    <div class="ico"><svg viewBox="0 0 24 24"><circle cx="18" cy="5" r="3"/><circle cx="6" cy="12" r="3"/><circle cx="18" cy="19" r="3"/><path d="M7 11l10-6 1 1.5-10 6zm0 2 10 6-1 1.5-10-6z"/></svg></div>
    www.bluewatergetaways.org/<br>community
  </div>

  <h2 class="panel-head media">IMAGES &amp; VIDEO</h2>
  <div class="c-block" style="top:446px">
    <div class="ico"><svg viewBox="0 0 24 24"><path d="M3 6h18v13H3zm7 3v7l6-3.5zM8 2l4 3 4-3 1 1-4 3h-2L7 3z"/></svg></div>
    <a>BLUEWATER VIDEO</a> to see<br>more photographs and video’s<br><a>LIKE</a> our COMMUNITY page
  </div>
  <div class="c-block" style="top:516px"><a>CLIENT LOGIN</a><br><a>cWV Film Festival</a></div>

  <h2 class="support">SUPPORT US</h2>
  <div class="merch" role="img" aria-label="Merchandise photo of brochures, a cap, a t-shirt and a drink bottle"></div>
  <a class="shop-btn"><svg viewBox="0 0 24 24"><path d="M3 3h18v4H3zM4 9h16v12h-6v-7H9v7H4z"/></svg>Our Shop</a>
</aside>

</body>
</html>
```